QM Studios needs and Interior Design Business card

I can do anything from Commercial to Residential and Free lance. Beginning to end in design selection process.
Need something to catch the eye of potential customers and vendors. From furniture to Tile and Cabinet selections. I can do it all.

Industry/Entity Type

Design Agency

Contact Information for Business Card

QM Studios- Design Consultanting Residential, Commerical
Maybe a cool detail background. Wall paper print that can have some texture

Font styles to use
Serif

Colors
709dcb
34a6d7
b868aa
e667a6
f59296
85acd3
ffffff
000000
5c5c5c

Requirements
Must have
• Square or Rectangular with Rounded edges
• Name
• Address
• Phone
• Email
Nice to have
• Some colored edges More simples not too busy
• Pattern detail in background.
Should not have
• Not too much color

```html
<!DOCTYPE html>
<html lang="en">
<head>
<meta charset="utf-8">
<title>QM Studios – Business Card</title>
<link rel="stylesheet" href="https://fonts.googleapis.com/css2?family=Arimo:wght@400;700&family=Questrial&display=swap">
<style>
  :root {
    --page: #e9e6e2;
    --card: #f1f1f1;
    --pink: #e5878c;
    --pink-soft: #f59296;
    --ink: #000000;
    --grey: #5c5c5c;
    --ghost: #dcdcdc;
    --white: #ffffff;
  }
  * { margin: 0; padding: 0; box-sizing: border-box; }
  html, body {
    width: 1200px; height: 902px; overflow: hidden;
    background: var(--page);
  }
  .canvas {
    width: 1200px; height: 902px;
    display: flex; flex-direction: column; align-items: center; justify-content: center;
    gap: 34px;
  }
  .card {
    position: relative;
    width: 700px; height: 400px;
    background: var(--card);
    border-radius: 14px;
    overflow: hidden;
    box-shadow: 0 6px 18px rgba(0,0,0,0.18);
  }
  .card-shapes { position: absolute; inset: 0; width: 100%; height: 100%; }

  /* back side */
  .ghost-circle {
    position: absolute; left: 330px; top: -60px;
    width: 340px; height: 340px; border-radius: 50%;
    border: 22px solid var(--ghost);
  }
  .services {
    position: absolute; left: 64px; top: 118px;
    list-style: none;
    font-family: "Arimo", sans-serif; font-size: 27px; color: var(--ink);
    line-height: 42px;
  }
  .services li { position: relative; padding-left: 34px; }
  .services li::before {
    content: ""; position: absolute; left: 0; top: 16px;
    width: 9px; height: 9px; border-radius: 50%;
    background: var(--pink-soft);
    box-shadow: 0 0 0 3px rgba(245,146,150,0.3);
  }
  .services .lead { padding-left: 34px; }
  .services .lead::before { display: none; }
  .back-name {
    position: absolute; left: 64px; bottom: 46px;
    font-family: "Questrial", sans-serif; font-size: 62px; letter-spacing: 14px;
    color: var(--pink);
  }

  /* front side */
  .brand {
    position: absolute; left: 40px; top: 70px; width: 270px;
    display: flex; flex-direction: column; align-items: center; gap: 28px;
  }
  .brand-circle {
    width: 120px; height: 120px; border-radius: 50%;
    border: 4px solid var(--ink);
  }
  .brand-name {
    font-family: "Questrial", sans-serif; font-size: 36px; letter-spacing: 7px;
    color: var(--ink); white-space: nowrap;
  }
  .person {
    position: absolute; right: 36px; top: 34px; text-align: right;
    font-family: "Arimo", sans-serif; color: var(--white);
  }
  .person-name { font-size: 34px; font-weight: 700; line-height: 1.1; }
  .person-role { font-size: 24px; line-height: 1.2; }
  .contact {
    position: absolute; right: 30px; top: 230px;
    list-style: none; text-align: right;
    font-family: "Arimo", sans-serif; font-size: 22px; color: var(--white);
    line-height: 40px;
  }
  .contact li { display: flex; align-items: center; justify-content: flex-end; gap: 12px; }
  .contact-icon { width: 22px; height: 22px; }
</style>
</head>
<body>
<main class="canvas">

  <section class="card card-back" aria-label="Card back">
    <div class="ghost-circle"></div>
    <ul class="services">
      <li>Interior Selections</li>
      <li>flooring</li>
      <li>cabinetry</li>
      <li>paint colors etc.</li>
    </ul>
    <div class="back-name">QM Studios</div>
  </section>

  <section class="card card-front" aria-label="Card front">
    <svg class="card-shapes" viewBox="0 0 700 400" preserveAspectRatio="none" aria-hidden="true">
      <polygon points="300,0 700,0 700,140 400,172" fill="var(--pink)"/>
      <polygon points="400,172 700,140 700,400 395,400" fill="var(--ink)"/>
      <polyline points="300,0 400,172 395,400" fill="none" stroke="var(--pink)" stroke-width="7"/>
      <line x1="400" y1="172" x2="700" y2="140" stroke="var(--ink)" stroke-width="5"/>
    </svg>

    <div class="brand">
      <div class="brand-circle"></div>
      <div class="brand-name">QM Studios</div>
    </div>

    <div class="person">
      <div class="person-name">Nora Whitfield</div>
      <div class="person-role">Design Consultant</div>
    </div>

    <ul class="contact">
      <li>021 555 0172
        <svg class="contact-icon" viewBox="0 0 22 22" aria-hidden="true">
          <rect width="22" height="22" rx="2" fill="var(--white)"/>
          <path d="M6 5h3l1 3-2 1.5a8 8 0 0 0 4.5 4.5L14 12l3 1v3c0 .6-.4 1-1 1A11 11 0 0 1 5 6c0-.6.4-1 1-1z" fill="var(--ink)"/>
        </svg>
      </li>
      <li>studio@qmstudios.com
        <svg class="contact-icon" viewBox="0 0 22 22" aria-hidden="true">
          <rect width="22" height="22" rx="2" fill="var(--white)"/>
          <rect x="4" y="6" width="14" height="10" fill="none" stroke="var(--ink)" stroke-width="1.6"/>
          <polyline points="4,6 11,12 18,6" fill="none" stroke="var(--ink)" stroke-width="1.6"/>
        </svg>
      </li>
    </ul>
  </section>

</main>
</body>
</html>
```